Rare Glow Edibles Gummies

Packaging design for custom mylars for cannabis infused gummies. I need a space for a warning label, nutrition facts, ingredients, brand logo and then individualized item details. We will later be doing assorted peanut butter cups, hard candies, etc.

```html
<!DOCTYPE html>
<html lang="en">
<head>
<meta charset="UTF-8">
<title>Rare Glow Edibles – Cannabis Infused Gummie Packaging</title>
<link rel="stylesheet" href="https://fonts.googleapis.com/css2?family=Arimo:wght@400;700&family=Roboto+Slab:wght@900&display=swap">
<style>
  :root {
    --canvas-bg: #f4f4f4;
    --panel-white: #ffffff;
    --panel-edge: #d9d9d9;
    --side-shade: #f3f3f3;
    --teal: #1f9c9c;
    --teal-dark: #137f80;
    --ink: #2b2b2b;
    --leaf-green: #4aa537;
    --leaf-deep: #1f6e1c;
    --warning-yellow: #f4d21f;
    --warning-red: #e02525;
    --white: #ffffff;
  }
  * { box-sizing: border-box; margin: 0; padding: 0; }
  html, body {
    width: 1200px; height: 1200px; overflow: hidden;
    background: var(--canvas-bg);
    font-family: "Arimo", Arial, sans-serif;
  }
  .package { position: relative; width: 1200px; height: 1200px; }

  /* Side panel: ingredients and nutrition facts */
  .side-panel {
    position: absolute; left: 200px; top: 250px;
    width: 170px; height: 680px;
    background: var(--side-shade);
    border: 2px solid var(--panel-edge);
  }
  .side-panel__content {
    position: absolute; left: 50%; top: 50%;
    width: 620px; transform: translate(-50%, -50%) rotate(-90deg);
    color: var(--ink);
  }
  .ingredients__title {
    font-weight: 700; font-size: 24px; letter-spacing: 2px;
    color: var(--teal); margin-bottom: 8px;
  }
  .ingredients__text { font-size: 16px; line-height: 1.45; }
  .nutrition__text { font-size: 16px; line-height: 1.45; margin-top: 4px; }
  .nutrition__label { font-weight: 700; }

  /* Front triangle panel */
  .front-panel {
    position: absolute; left: 400px; top: 200px;
    width: 740px; height: 740px;
  }
  .front-panel__art { position: absolute; inset: 0; }

  .brand {
    position: absolute; left: 0; right: 0; top: 326px;
    display: flex; align-items: center; justify-content: center; gap: 10px;
  }
  .brand__dot {
    width: 30px; height: 30px; border-radius: 50%;
    border: 2px solid var(--teal);
  }
  .brand__name { font-size: 19px; font-weight: 700; color: var(--teal); }

  .product-title {
    position: absolute; left: 0; right: 0; top: 405px;
    text-align: center; color: var(--teal); font-weight: 400;
  }
  .product-title__line1 { font-size: 32px; letter-spacing: 0.5px; }
  .product-title__line2 {
    display: inline-block; font-size: 56px; font-weight: 700;
    line-height: 1; color: var(--teal-dark);
  }

  .warning-label {
    position: absolute; left: 225px; top: 528px;
    width: 300px; height: 60px;
    display: flex; border-radius: 8px; overflow: hidden;
  }
  .warning-label__icon {
    width: 66px; background: var(--warning-yellow);
    display: flex; align-items: center; justify-content: center;
  }
  .warning-label__body {
    flex: 1; background: var(--warning-red); color: var(--white);
    padding: 5px 8px;
  }
  .warning-label__title {
    font-family: "Roboto Slab", Georgia, serif; font-weight: 900;
    font-size: 23px; line-height: 1;
  }
  .warning-label__text { font-size: 8.5px; line-height: 1.25; margin-top: 3px; }

  .net-weight {
    position: absolute; left: 230px; top: 604px;
    font-size: 15px; font-weight: 700; color: var(--teal);
  }
</style>
</head>
<body>
<main class="package">

  <section class="side-panel">
    <div class="side-panel__content">
      <h2 class="ingredients__title">INGREDIENTS:</h2>
      <p class="ingredients__text">Glucose syrup, sugar, water, pectin, citric acid, natural fruit flavors, cannabis extract, coconut oil, carnauba wax.</p>
      <p class="nutrition__text"><span class="nutrition__label">Nutrition per piece:</span> 15 calories, 0g fat, 4g carbs, 3g sugar, 0g protein, 5mg THC.</p>
    </div>
  </section>

  <section class="front-panel">
    <svg class="front-panel__art" width="740" height="740" viewBox="0 0 740 740">
      <defs>
        <clipPath id="triangle-clip">
          <polygon points="370,50 720,710 20,710"/>
        </clipPath>
        <radialGradient id="leaf-tone">
          <stop offset="0" stop-color="var(--leaf-green)"/>
          <stop offset="0.6" stop-color="var(--leaf-deep)"/>
          <stop offset="1" stop-color="var(--leaf-deep)" stop-opacity="0"/>
        </radialGradient>
      </defs>
      <polygon points="370,50 720,710 20,710" fill="var(--panel-white)" stroke="var(--panel-edge)" stroke-width="2"/>
      <g clip-path="url(#triangle-clip)">
        <circle cx="405" cy="200" r="58" fill="url(#leaf-tone)" role="img" aria-label="Cannabis leaf illustration"/>
        <circle cx="215" cy="335" r="38" fill="url(#leaf-tone)" role="img" aria-label="Cannabis leaf illustration"/>
        <circle cx="525" cy="335" r="36" fill="url(#leaf-tone)" role="img" aria-label="Cannabis leaf illustration"/>
        <circle cx="150" cy="645" r="62" fill="url(#leaf-tone)" role="img" aria-label="Cannabis leaf illustration"/>
        <circle cx="600" cy="605" r="56" fill="url(#leaf-tone)" role="img" aria-label="Cannabis leaf illustration"/>
      </g>
    </svg>

    <div class="brand">
      <span class="brand__dot"></span>
      <span class="brand__name">Rare Glow Edibles</span>
    </div>

    <h1 class="product-title">
      <span class="product-title__line1">CANNABIS INFUSED</span><br>
      <span class="product-title__line2">GUMMIE</span>
    </h1>

    <div class="warning-label">
      <div class="warning-label__icon">
        <svg width="40" height="36" viewBox="0 0 40 36" aria-hidden="true">
          <path d="M20 3 L37 33 L3 33 Z" fill="none" stroke="var(--warning-red)" stroke-width="3.5" stroke-linejoin="round"/>
          <rect x="18.2" y="12" width="3.6" height="11" rx="1.5" fill="var(--warning-red)"/>
          <circle cx="20" cy="27.5" r="2.1" fill="var(--warning-red)"/>
        </svg>
      </div>
      <div class="warning-label__body">
        <div class="warning-label__title">WARNING</div>
        <p class="warning-label__text">Contains THC. Keep out of reach of children and pets. For adults 21 and over only.</p>
      </div>
    </div>

    <p class="net-weight">Net weight: 150g</p>
  </section>

</main>
</body>
</html>
```